依頼詳細
現在使っているものを画像データで添付します。
事務所ロゴをフォトショップデータで添付します。

参考に、市販の表紙デザインにはこういったものがあります。(下記リンク)
https://www.kazane-dk.co.jp/store/products/list.php?category_id=23
https://tomoriworks.com/item/certificate/
http://mizuho-kanade.com/front_cover/
A4の紙を綴じるものなので、A3より一回り大きいA3ワイドのレザック紙に印刷しております。こちら302×430mmサイズです。

表紙には、お客様(権利者)の名前と
その下には不動産の表示が入ります。(案件ごとに印刷します)
そのため、こちらを手差し印刷できるよう、高さ5センチ程度の空白を空けておいていただきたいです。

サイズ:A3ワイド(302×430mm)
2つ折り、左開きです。半分に折った部分が表紙となります。

色、デザインの雰囲気等お任せいたします。
公的で固い重要書類をいれるものですが、そういったイメージにはあまり縛られずなるべくオリジナリティのあるものを使いたいと思います。
記載項目
不動産登記権利情報

司法書士ふじさわ事務所
希望イメージ
シンプル 複雑
単色 カラフル
暗い 明るい
日常 高級
遊び心 厳粛
未来的 伝統的
女性的 男性的
希望する色
設定なし
納品ファイル
• イラストレーター形式 (.ai)
補足説明
設定なし
【追記】桐のマークについて
現在使っている権利証表紙には、司法書士バッヂの意匠である五三桐花をいれておりますが、今回は特に使用の指定はしません。
桐のマークを入れる場合については、五三桐でお願いいたします(葉っぱが中央に5枚・左右に3枚ずつの家紋)

(参考)
http://senra-mokudo.com/kamon-c/cate0/kiri/kiri2.html
https://www.ezukan-store.jp/img344/225970_3130817.html
■ 選んだ理由

見た瞬間に目を惹くデザインだと思い、選ばせていただきました。

■ 提案者全員のお礼・コメント

たくさんのご提案をいただき大変嬉しく思っております。
皆様それぞれ、素敵なデザインを考えていただき本当にありがとうございます。

```html
<!DOCTYPE html>
<html lang="ja">
<head>
<meta charset="utf-8">
<title>不動産登記権利情報 表紙</title>
<link rel="stylesheet" href="https://fonts.googleapis.com/css2?family=Shippori+Mincho:wght@500;700&family=Noto+Sans+JP:wght@400;700&display=swap">
<style>
  :root {
    --paper: #dcebdf;
    --paper-light: #e8f3ea;
    --ink-green: #1f7a3c;
    --ink-deep: #17612f;
    --ornament-tone: #8fc19c;
  }
  * { margin: 0; padding: 0; box-sizing: border-box; }
  html, body { width: 851px; height: 1200px; overflow: hidden; background: #ffffff; }
  .cover {
    position: relative;
    width: 851px;
    height: 1200px;
    background: radial-gradient(ellipse at 50% 45%, var(--paper-light) 0%, var(--paper) 75%);
    overflow: hidden;
  }
  .frame { position: absolute; inset: 0; }
  .crest {
    position: absolute;
    left: 355px; top: 140px;
    width: 140px; height: 110px;
    border-radius: 50%;
    background: radial-gradient(circle, var(--ink-green) 0%, var(--ink-deep) 70%);
    opacity: 0.9;
  }
  .title {
    position: absolute;
    left: 0; right: 0; top: 318px;
    text-align: center;
    font-family: "Shippori Mincho", serif;
    font-weight: 700;
    font-size: 46px;
    letter-spacing: 2px;
    color: var(--ink-deep);
  }
  .quill-art {
    position: absolute;
    left: 560px; top: 650px;
    width: 250px; height: 330px;
    background: linear-gradient(150deg, var(--ink-green) 0%, var(--ornament-tone) 55%, var(--paper-light) 100%);
    border-radius: 120px 20px 60px 20px;
    opacity: 0.75;
  }
  .office {
    position: absolute;
    left: 285px; top: 1010px;
    display: flex;
    align-items: center;
    gap: 16px;
    color: var(--ink-deep);
  }
  .office-mark {
    width: 56px; height: 56px;
    background: var(--ink-deep);
    flex-shrink: 0;
  }
  .office-text { display: flex; flex-direction: column; }
  .office-role {
    font-family: "Shippori Mincho", serif;
    font-weight: 700;
    font-size: 17px;
    letter-spacing: 3px;
    text-align: center;
  }
  .office-name {
    font-family: "Shippori Mincho", serif;
    font-weight: 700;
    font-size: 40px;
    letter-spacing: 2px;
    line-height: 1.2;
  }
  .office-contact {
    font-family: "Noto Sans JP", sans-serif;
    font-size: 10px;
    line-height: 1.5;
    margin-top: 4px;
  }
</style>
</head>
<body>
<main class="cover">
  <svg class="frame" width="851" height="1200" viewBox="0 0 851 1200" aria-hidden="true">
    <g fill="none" stroke="var(--ink-green)">
      <rect x="24" y="24" width="803" height="1152" stroke-width="5"/>
      <rect x="36" y="36" width="779" height="1128" stroke-width="1.5"/>
      <rect x="58" y="58" width="735" height="1084" stroke-width="2"/>
      <rect x="170" y="270" width="511" height="160" rx="18" stroke-width="2"/>
      <rect x="180" y="280" width="491" height="140" rx="12" stroke-width="1"/>
      <line x1="200" y1="660" x2="651" y2="660" stroke-width="2"/>
      <line x1="240" y1="668" x2="611" y2="668" stroke-width="1"/>
    </g>
  </svg>

  <div class="crest" role="img" aria-label="五三桐の家紋"></div>

  <h1 class="title">不動産登記権利情報</h1>

  <div class="quill-art" role="img" aria-label="羽根ペンと巻物のイラスト"></div>

  <footer class="office">
    <span class="office-mark"></span>
    <div class="office-text">
      <span class="office-role">司法書士・行政書士</span>
      <span class="office-name">ふじさわ事務所</span>
      <span class="office-contact">〒060-0000 北海道札幌市中央区北一条西1丁目<br>TEL 011-000-0000　FAX 011-000-0001</span>
    </div>
  </footer>
</main>
</body>
</html>
```